Business Card Design

Velvet Pixel Promotions

An online marketing consulting & strategy business for the cosmetic niche

We specialise in Increasing Leads, Conversions & Content Marketing

I am looking for a very clean, BOLD business card that is simple & effective

Target Market(s)

cosmetic surgeons & cosmetic clinics

Industry/Entity Type

Marketing

Contact Information for Business Card

Darren Okoye
Online Marketing Strategist

Darren@VelvetPixelPromotions.example
0491 268 517

LinkedIn: in/darrenokoye

```html
<!DOCTYPE html>
<html lang="en">
<head>
<meta charset="UTF-8">
<title>Velvet Pixel Promotions – Business Card</title>
<link rel="stylesheet" href="https://fonts.googleapis.com/css2?family=Stardos+Stencil:wght@700&display=swap">
<style>
  :root {
    --ink: #1f1f1f;
    --plum: #6b1f4a;
    --link: #1a2fd6;
    --paper: #ffffff;
  }
  * { box-sizing: border-box; margin: 0; padding: 0; }
  html, body {
    width: 1200px;
    height: 682px;
    overflow: hidden;
    background: var(--paper);
  }
  .card {
    position: relative;
    width: 1200px;
    height: 682px;
    background: var(--paper);
    color: var(--ink);
    font-family: "Stardos Stencil", "Arial Black", sans-serif;
    font-weight: 700;
  }
  .rule {
    position: absolute;
    left: 19px;
    right: 19px;
    height: 0;
    border-top: 5px dotted var(--ink);
  }
  .rule--top { top: 26px; }
  .rule--bottom { top: 626px; }

  .contact-head {
    position: absolute;
    top: 44px;
    right: 18px;
    text-align: right;
    text-transform: uppercase;
    line-height: 1.15;
  }
  .contact-head__name { font-size: 27px; letter-spacing: 0.5px; }
  .contact-head__tel { font-size: 19px; margin-top: 4px; }

  .brand-mark {
    position: absolute;
    left: 80px;
    top: 150px;
    width: 340px;
    height: 340px;
    border-radius: 50%;
    background: var(--plum);
  }

  .brand-name {
    position: absolute;
    left: 470px;
    top: 262px;
    width: 700px;
    text-align: center;
    text-transform: uppercase;
    font-size: 68px;
    line-height: 1.3;
    letter-spacing: 3px;
    color: var(--ink);
  }

  .footer {
    position: absolute;
    left: 19px;
    right: 19px;
    top: 648px;
    display: flex;
    justify-content: space-between;
    align-items: baseline;
    text-transform: uppercase;
    font-size: 17px;
    white-space: nowrap;
  }
  .footer__email {
    color: var(--link);
    text-decoration: underline;
  }
</style>
</head>
<body>
  <div class="card">
    <div class="rule rule--top"></div>

    <header class="contact-head">
      <div class="contact-head__name">Darren Okoye</div>
      <div class="contact-head__tel">Tel: 0491 268 517</div>
    </header>

    <div class="brand-mark" aria-hidden="true"></div>

    <h1 class="brand-name">Velvet Pixel<br>Promotions</h1>

    <div class="rule rule--bottom"></div>

    <footer class="footer">
      <span class="footer__role">Online Marketing Strategist : <a class="footer__email" href="mailto:Darren@VelvetPixelPromotions.example">Darren@VelvetPixelPromotions.example</a></span>
      <span class="footer__linkedin">LinkedIn: in/darrenokoye</span>
    </footer>
  </div>
</body>
</html>
```